Business cards and stationery for small forestry/oilfield consulting company
Pine Ledger Consulting Ltd
Business cards and stationery for small forestry/oilfield consulting company - Environment
Creative Brief
Professional
K.J. Dorrin Waltby
RPFT
Box 42 Site 7 RR5 Alberta, Canada T0X 9Q7
pineledger@quorvanet.ca
The name of Pine Ledger Consulting Ltd is in the logo itself, not needed to repeat unless somehow artistically beneficial
Concepts
Business Cards, Letterhead, and Envelopes

```html
<!DOCTYPE html>
<html lang="en">
<head>
<meta charset="utf-8">
<title>Pine Ledger Consulting Ltd – Stationery Concepts</title>
<link href="https://fonts.googleapis.com/css2?family=Cinzel:wght@700&family=Open+Sans:wght@400;600&display=swap" rel="stylesheet">
<style>
  :root{
    --backdrop:#4b3023;
    --paper:#ffffff;
    --paper-shade:#eef0ef;
    --brand-green:#1e6a55;
    --brand-green-dark:#174f40;
    --flap-grey:#3c3f3e;
    --ink:#4a4f4d;
    --label:#d9cfc6;
  }
  *{margin:0;padding:0;box-sizing:border-box}
  html,body{width:1200px;height:466px;overflow:hidden;background:var(--backdrop)}
  .canvas{position:relative;width:1200px;height:466px;font-family:"Open Sans",Arial,sans-serif;color:var(--ink)}
  .label{position:absolute;font-size:5.5px;letter-spacing:.8px;text-transform:uppercase;color:var(--label);font-weight:600;white-space:nowrap}
  .sheet{position:absolute;background:var(--paper);box-shadow:0 2px 6px rgba(0,0,0,.35)}
  .brand{font-family:"Cinzel",Georgia,serif;font-weight:700;color:var(--brand-green);text-align:center;line-height:1}
  .brand .name{display:block;letter-spacing:.5px}
  .brand .sub{display:block;letter-spacing:1.5px;margin-top:2px}
  .contact{font-size:4.6px;line-height:7px;color:var(--ink)}
  .contact .row{display:flex;align-items:center;gap:3px;white-space:nowrap}
  .contact .dot{width:4px;height:4px;border-radius:50%;background:var(--brand-green);flex:none}

  /* business cards */
  .card{width:72px;height:46px;border:1.5px solid var(--brand-green)}
  .card-front{left:19px;top:211px;padding:5px}
  .card-front .brand .name{font-size:6px}
  .card-front .brand .sub{font-size:2.6px}
  .card-front .contact{font-size:2.4px;line-height:3.6px;margin-top:5px}
  .card-back{left:19px;top:331px;display:flex;align-items:center;justify-content:center}
  .card-back .brand .name{font-size:7px}
  .card-back .brand .sub{font-size:3px}

  /* letterheads */
  .letterhead{top:29px;width:302px;height:398px;border:4px solid var(--brand-green)}
  .lh-one{left:149px;padding:14px 18px}
  .lh-one .top{display:flex;justify-content:space-between;align-items:flex-start}
  .lh-one .brand .name{font-size:17px}
  .lh-one .brand .sub{font-size:6.5px}
  .lh-two{left:485px;padding:14px 18px}
  .lh-two .brand{margin:0 auto;width:max-content}
  .lh-two .brand .name{font-size:17px}
  .lh-two .brand .sub{font-size:6.5px}
  .lh-two .footer{position:absolute;left:18px;right:18px;bottom:12px;display:flex;justify-content:center;gap:10px;font-size:4.2px}

  /* envelopes */
  .env{width:276px;height:50px;left:852px}
  .env-flap{position:absolute;left:0;top:0;width:100%;height:100%}
  .env-green{top:22px;height:60px;background:var(--paper)}
  .env-dark{top:92px;background:var(--paper)}
  .env-front{top:148px;border-bottom:4px solid var(--brand-green);display:flex;align-items:center;justify-content:center}
  .env-front .brand .name{font-size:9px}
  .env-front .brand .sub{font-size:3.6px}
  .env-back{top:206px;height:56px;background:var(--paper-shade)}
  .env-two{left:790px;top:283px;width:318px;height:128px;border:4px solid var(--brand-green);padding:10px 14px}
  .env-two .brand{text-align:left}
  .env-two .brand .name{font-size:11px}
  .env-two .brand .sub{font-size:4.2px}
  .env-two .contact{font-size:3.6px;line-height:5px;margin-top:4px}
</style>
</head>
<body>
<main class="canvas">
  <span class="label" style="left:20px;top:195px">Stationery Concepts</span>

  <section class="sheet card card-front">
    <div class="brand"><span class="name">PINE LEDGER</span><span class="sub">CONSULTING LTD</span></div>
    <div class="contact">
      <div>K.J. Dorrin Waltby, RPFT</div>
      <div>Box 42 Site 7 RR5 Alberta, Canada T0X 9Q7</div>
      <div>pineledger@quorvanet.ca</div>
    </div>
  </section>
  <span class="label" style="left:21px;top:265px">Business Card Front</span>

  <section class="sheet card card-back">
    <div class="brand"><span class="name">PINE LEDGER</span><span class="sub">CONSULTING LTD</span></div>
  </section>
  <span class="label" style="left:22px;top:385px">Business Card Back</span>

  <section class="sheet letterhead lh-one">
    <div class="top">
      <div class="brand"><span class="name">PINE LEDGER</span><span class="sub">CONSULTING LTD</span></div>
      <div class="contact">
        <div class="row"><span class="dot"></span>K.J. Dorrin Waltby, RPFT</div>
        <div class="row"><span class="dot"></span>Tel 403 555 0142</div>
        <div class="row"><span class="dot"></span>Box 42 Site 7 RR5</div>
        <div class="row"><span class="dot"></span>Alberta, Canada T0X 9Q7</div>
        <div class="row"><span class="dot"></span>pineledger@quorvanet.ca</div>
      </div>
    </div>
  </section>
  <span class="label" style="left:272px;top:434px">Letter Head Option 1</span>

  <section class="sheet letterhead lh-two">
    <div class="brand"><span class="name">PINE LEDGER</span><span class="sub">CONSULTING LTD</span></div>
    <div class="footer contact">
      <span>K.J. Dorrin Waltby, RPFT</span>
      <span>Box 42 Site 7 RR5 Alberta, Canada T0X 9Q7</span>
      <span>pineledger@quorvanet.ca</span>
    </div>
  </section>
  <span class="label" style="left:606px;top:434px">Letter Head Option 2</span>

  <section class="sheet env env-green">
    <svg class="env-flap" viewBox="0 0 276 60" preserveAspectRatio="none" aria-hidden="true">
      <path d="M0 0H276V24Q276 30 268 31L150 44Q138 46 126 44L8 31Q0 30 0 24Z" fill="var(--brand-green)"/>
    </svg>
  </section>
  <section class="sheet env env-dark">
    <svg class="env-flap" viewBox="0 0 276 50" preserveAspectRatio="none" aria-hidden="true">
      <path d="M0 0H276V18Q276 24 268 25L150 36Q138 38 126 36L8 25Q0 24 0 18Z" fill="var(--flap-grey)"/>
    </svg>
  </section>
  <section class="sheet env env-front">
    <div class="brand"><span class="name">PINE LEDGER</span><span class="sub">CONSULTING LTD</span></div>
  </section>
  <section class="sheet env env-back">
    <svg class="env-flap" viewBox="0 0 276 56" preserveAspectRatio="none" aria-hidden="true">
      <path d="M0 0H276V20Q276 26 268 27L150 40Q138 42 126 40L8 27Q0 26 0 20Z" fill="var(--paper)"/>
      <path d="M0 56L120 40M276 56L156 40" stroke="#d6dbd9" stroke-width="1" fill="none"/>
    </svg>
  </section>
  <span class="label" style="left:1137px;top:120px;transform:rotate(90deg);transform-origin:left top">Envelope Option 1</span>

  <section class="sheet env-two">
    <div class="brand"><span class="name">PINE LEDGER</span><span class="sub">CONSULTING LTD</span></div>
    <div class="contact">
      <div>Box 42 Site 7 RR5</div>
      <div>Alberta, Canada T0X 9Q7</div>
    </div>
  </section>
  <span class="label" style="left:920px;top:418px">Envelope Option 2</span>
</main>
</body>
</html>
```